Revamp Current Website From 2012 TO 2018

We need a ravamp to our current website. I prefer a professional corporate modern feel to it.

My Current Website is www.brightlanepromoworks.biz. Please redesign the homepage and the /certs page first....see attached document for specific instructions..

There is a lot of content at the bottom but maybe we can shorten that by using titles and a pop up of the details or something so it doesnt take too mcuh space...or maybe a red more hyperlink to see the rest of info in pop up or something or new page...

Target Market(s)

B2B, business owners, website owners, marketing companies.

Industry/Entity Type

Promotional Product

Number of Pages Required

2 page

Colors

Designer to choose colors to be used in the design.

Requirements
Must have
• Please keep in mind logo mock up I am working on that looks beautiful on dark background for header...see attached for logo
• Must use existing content I hope your marketing mind comes in to play when designing the website.
• Must have all my content provided on each page...
Nice to have
• similiar color scheme...
Should not have
• I dont like using templates because usually hard to expand on design in future so Prefer full custom designs
• Please no templates

```html
<!DOCTYPE html>
<html lang="en">
<head>
<meta charset="utf-8">
<title>Brightlane Promoworks – Home</title>
<link href="https://fonts.googleapis.com/css2?family=Arimo:wght@400;700&family=Open+Sans:wght@400;600;700&display=swap" rel="stylesheet">
<style>
:root{
  --blue:#1eaee8;
  --blue-deep:#0f8fc7;
  --teal-band:#0d5f7e;
  --ink:#222426;
  --dark:#1b1d21;
  --slate:#4b4e54;
  --white:#ffffff;
  --muted:#555a60;
  --navy:#16263a;
}
*{margin:0;padding:0;box-sizing:border-box}
html,body{width:1200px;height:3103px;overflow:hidden}
body{font-family:"Open Sans",Arial,sans-serif;color:var(--ink);background:var(--white)}
.heading{font-family:"Arimo",Arial,sans-serif}

/* header */
.site-header{height:124px;background:linear-gradient(180deg,#24262b,#141518);position:relative}
.brand{position:absolute;left:79px;top:40px;display:flex;align-items:center;gap:12px}
.brand-square{width:32px;height:32px;background:var(--blue)}
.brand-name{font-family:"Arimo",Arial,sans-serif;font-weight:700;font-size:27px;color:var(--blue);letter-spacing:1.5px;text-transform:uppercase}
.contact{position:absolute;right:80px;top:10px;text-align:right;color:var(--white);font-size:24px}
.contact-row{display:flex;align-items:center;justify-content:flex-end;gap:12px;height:56px}
.contact-row b{font-weight:700;font-size:23px}
.phone-icon{width:40px;height:40px;border:2px solid #fff;border-radius:50%;display:flex;align-items:center;justify-content:center}

/* nav */
.main-nav{height:58px;background:linear-gradient(180deg,#55585c,#2f3134);display:flex;padding-left:78px}
.main-nav a{color:#fff;text-decoration:none;font-size:15.5px;font-weight:700;text-transform:uppercase;padding:0 21px;line-height:58px;border-right:1px solid #2a2b2e}
.main-nav a.active{background:var(--blue)}

/* hero */
.hero{height:517px;position:relative;background:#f7f8fa;overflow:hidden}
.hero-photo{position:absolute;left:0;top:0;right:0;bottom:0;
  background:
    radial-gradient(ellipse 160px 120px at 1010px 470px,rgba(120,200,255,.55),rgba(120,200,255,0)),
    radial-gradient(ellipse 260px 340px at 840px 300px,rgba(24,34,52,.95),rgba(24,34,52,0)),
    radial-gradient(ellipse 200px 300px at 1110px 200px,rgba(60,110,160,.8),rgba(60,110,160,0)),
    linear-gradient(90deg,#ffffff 0%,#f7f8fa 36%,#d7dde4 52%,#7d8da0 68%,#34465d 84%,#263850 100%)}
.hero-copy{position:absolute;left:80px;top:140px;width:490px}
.hero-copy p{font-size:25px;line-height:31px;color:#222}
.btn{display:inline-block;background:var(--blue);color:#fff;font-weight:700;font-size:18px;border-radius:26px;padding:12px 24px;text-decoration:none}
.hero-copy .btn{margin-top:28px}

/* welcome */
.welcome{height:311px;background:var(--blue);position:relative}
.welcome-photo{position:absolute;left:45px;top:36px;width:395px;height:275px;
  background:
    radial-gradient(ellipse 90px 70px at 90px 190px,rgba(25,25,28,.9),rgba(25,25,28,0)),
    radial-gradient(ellipse 60px 80px at 250px 90px,rgba(40,30,28,.85),rgba(40,30,28,0)),
    radial-gradient(ellipse 190px 120px at 200px 190px,#f4f4f4 0%,#e6eaee 55%,rgba(30,174,232,0) 100%)}
.welcome-copy{position:absolute;left:476px;top:48px;width:660px;color:#fff}
.welcome-copy h1{font-size:42px;line-height:47px;font-weight:400;color:#1a1a1a}
.welcome-copy h1 + h1{color:#fff}
.welcome-copy p{margin-top:16px;font-size:15px;line-height:25px}
.stats{height:124px;background:var(--teal-band);display:grid;grid-template-columns:repeat(6,1fr);color:#fff;text-align:center;align-items:center;padding:0 40px}
.stat strong{display:block;font-weight:400;font-size:20px;line-height:24px}
.stat span{font-size:15px;line-height:19px;display:block}

/* four ways */
.ways{height:480px;background:#efefef;text-align:center;padding-top:52px}
.section-title{font-family:"Arimo",Arial,sans-serif;font-size:43px;line-height:47px;font-weight:400;color:#222}
.section-title em{font-style:normal;color:var(--blue)}
.ways-grid{display:grid;grid-template-columns:repeat(4,271px);justify-content:center;margin-top:28px}
.way-icon{width:126px;height:126px;margin:0 auto;border-radius:50%;background:var(--blue);border:7px solid #fff;box-shadow:0 0 0 2px var(--blue);display:flex;align-items:center;justify-content:center}
.way h3{font-size:24px;font-weight:400;margin-top:12px;color:#222}
.way p{font-size:15px;line-height:25px;color:var(--muted);margin:2px auto 0;width:236px}

/* boost */
.boost{height:290px;display:flex}
.boost-copy{width:400px;background:var(--slate);color:#fff;text-align:center;padding:30px 26px}
.boost-copy h2{font-size:27px;line-height:30px;font-weight:700}
.boost-copy p{font-size:15px;line-height:25px;margin-top:16px}
.boost-photo-a{width:401px;
  background:
    radial-gradient(ellipse 60px 50px at 245px 185px,rgba(240,240,235,.9),rgba(240,240,235,0)),
    radial-gradient(ellipse 70px 120px at 270px 90px,rgba(60,45,40,.75),rgba(60,45,40,0)),
    radial-gradient(ellipse 110px 50px at 80px 150px,rgba(70,90,70,.7),rgba(70,90,70,0)),
    linear-gradient(180deg,#f1f4f6 0%,#dfe6ea 35%,#8fa6a8 52%,#5f7f86 66%,#7a5a44 82%,#4a3428 100%)}
.boost-photo-b{flex:1;
  background:
    radial-gradient(ellipse 150px 60px at 240px 200px,rgba(70,72,76,.8),rgba(70,72,76,0)),
    radial-gradient(ellipse 90px 200px at 340px 120px,rgba(110,140,90,.55),rgba(110,140,90,0)),
    linear-gradient(90deg,#f4f2ee 0%,#e2ded7 40%,#b9b4ab 70%,#8a8580 100%)}

/* plug in */
.plug{height:383px;background:linear-gradient(rgba(30,174,232,.86),rgba(30,174,232,.86)),linear-gradient(90deg,#6f98ab,#c4d6df,#8fb2c2,#d7e2e7,#7fa6b8);text-align:center;position:relative;padding-top:52px}
.plug .section-title{color:#1a1a1a;font-weight:700}
.plug-grid{display:grid;grid-template-columns:repeat(4,271px);justify-content:center;margin-top:30px}
.plug-icon{width:103px;height:103px;border-radius:50%;background:#3b3d40;margin:0 auto;display:flex;align-items:center;justify-content:center}
.plug-item h3{color:#fff;font-size:23px;font-weight:400;margin-top:16px}
.plug-tip{position:absolute;left:62px;top:364px;width:260px;background:#fff;border-radius:14px;border:1px solid #bbb;font-size:14.5px;line-height:25px;color:#555;padding:8px 10px;text-align:center;z-index:2}
.plug-tip::before{content:"";position:absolute;left:118px;top:-12px;border:12px solid transparent;border-top:0;border-bottom-color:#fff}

/* clients */
.clients{height:311px;text-align:center;padding-top:58px}
.clients-grid{display:grid;grid-template-columns:repeat(4,240px);gap:29px;justify-content:center;margin-top:32px}
.client{height:122px;border:1px solid #cfd3d6;display:flex;align-items:center;justify-content:center;gap:10px;font-size:24px;font-weight:700;color:#2e3d63}
.client i{width:16px;height:16px;background:#2e3d63;display:block}

/* cta */
.cta{height:320px;background:linear-gradient(180deg,#34b8ec,#1b9fd8);text-align:center;padding-top:46px}
.cta h2{font-family:"Arimo",Arial,sans-serif;font-size:44px;line-height:47px;font-weight:400;letter-spacing:1px;color:#1a1a1a}
.cta h2 span{color:#fff}
.btn-dark{display:inline-block;margin-top:30px;width:166px;background:#3d4044;border:2px solid #fff;color:#fff;font-size:18px;font-weight:600;line-height:46px;border-radius:26px;text-decoration:none}

/* footer */
.site-footer{height:186px;background:#0f1012;text-align:center;position:relative;padding-top:62px}
.to-top{position:absolute;left:578px;top:-22px;width:44px;height:44px;background:#fff;transform:rotate(45deg)}
.to-top svg{transform:rotate(-45deg)}
.footer-brand{display:inline-flex;align-items:center;gap:10px;background:#1d2024;width:406px;height:62px;justify-content:center}
.footer-brand .brand-square{width:22px;height:22px}
.footer-brand .brand-name{font-size:23px}
.copyright{color:#fff;font-size:15px;margin-top:20px}
</style>
</head>
<body>

<header class="site-header">
  <div class="brand"><span class="brand-square"></span><span class="brand-name">Brightlane Promoworks</span></div>
  <div class="contact">
    <div class="contact-row">USA Office <span class="phone-icon"><svg width="18" height="18" viewBox="0 0 24 24"><path fill="#fff" d="M6.6 10.8a15 15 0 0 0 6.6 6.6l2.2-2.2c.3-.3.7-.4 1-.2 1.1.4 2.3.6 3.6.6.6 0 1 .4 1 1V20c0 .6-.4 1-1 1A17 17 0 0 1 3 4c0-.6.4-1 1-1h3.5c.6 0 1 .4 1 1 0 1.3.2 2.5.6 3.6.1.3 0 .7-.2 1z"/></svg></span><b>555-014-2290</b></div>
    <div class="contact-row">International <span class="phone-icon"><svg width="18" height="18" viewBox="0 0 24 24"><path fill="#fff" d="M6.6 10.8a15 15 0 0 0 6.6 6.6l2.2-2.2c.3-.3.7-.4 1-.2 1.1.4 2.3.6 3.6.6.6 0 1 .4 1 1V20c0 .6-.4 1-1 1A17 17 0 0 1 3 4c0-.6.4-1 1-1h3.5c.6 0 1 .4 1 1 0 1.3.2 2.5.6 3.6.1.3 0 .7-.2 1z"/></svg></span><b>1-800-555-0147</b></div>
  </div>
</header>

<nav class="main-nav">
  <a class="active" href="#">Home</a><a href="#">Our Incentives</a><a href="#">Samples</a><a href="#">How It Works</a><a href="#">Testimonials</a><a href="#">FAQ</a><a href="#">Contact</a><a href="#">Sign Up</a><a href="#">Log In</a>
</nav>

<section class="hero">
  <div class="hero-photo" role="img" aria-label="Businessman in a dark suit overlaid with a glowing city skyline and rising chart lines"></div>
  <div class="hero-copy">
    <p>Increase Leads &amp; Sales From Your Existing Marketing Efforts By Offering High Perceived Value Incentives To Your Customers!</p>
    <a class="btn" href="#">30 DAY RISK FREE TRIAL</a>
  </div>
</section>

<section class="welcome">
  <div class="welcome-photo" role="img" aria-label="Smiling businesswoman working at a laptop"></div>
  <div class="welcome-copy">
    <h1 class="heading">Welcome To</h1>
    <h1 class="heading">Brightlane Promoworks</h1>
    <p>Create a variety giveaway promotions for your business with an unlimited supply of top quality vacation getaway certificates, restaurant gift certificates, electronic product giveaways and gas or grocery rewards for just $99/mth. Whether you need 100 or 100,000 you will never pay more than $99.</p>
  </div>
</section>
<div class="stats">
  <div class="stat"><strong>12</strong><span>Years In<br>Business</span></div>
  <div class="stat"><strong>13,000+</strong><span>Clients<br>Enrolled</span></div>
  <div class="stat"><strong>2+ Million</strong><span>Certificates In<br>Circulation</span></div>
  <div class="stat"><strong>170,000+</strong><span>Redemptions<br>To Date</span></div>
  <div class="stat"><strong>A</strong><span>Rating TCB</span></div>
  <div class="stat"><strong>Licensed<br>Seller</strong><span>Of Travel CST<br>#4408127</span></div>
</div>

<section class="ways">
  <h2 class="section-title">Give Away Unlimited Incentives To Your<br>Customers <em>Four Easy Ways !</em></h2>
  <div class="ways-grid">
    <div class="way">
      <div class="way-icon"><svg width="60" height="56" viewBox="0 0 60 56"><rect x="14" y="2" width="32" height="14" fill="#fff"/><rect x="2" y="16" width="56" height="24" rx="4" fill="#fff"/><rect x="14" y="32" width="32" height="22" fill="#fff" stroke="#1eaee8" stroke-width="3"/><line x1="20" y1="40" x2="40" y2="40" stroke="#1eaee8" stroke-width="2"/><line x1="20" y1="46" x2="40" y2="46" stroke="#1eaee8" stroke-width="2"/></svg></div>
      <h3>Print</h3><p>Download PDF certificates to print and physically hand them out or mail them to...</p>
    </div>
    <div class="way">
      <div class="way-icon"><svg width="60" height="50" viewBox="0 0 60 50"><rect x="2" y="14" width="56" height="34" fill="#fff"/><path d="M2 14 30 34 58 14" fill="none" stroke="#1eaee8" stroke-width="3"/><rect x="16" y="2" width="28" height="22" fill="#fff" stroke="#1eaee8" stroke-width="2"/></svg></div>
      <h3>Email</h3><p>Email e-certificates to your customers individually or in bulk with just one click!</p>
    </div>
    <div class="way">
      <div class="way-icon"><svg width="60" height="60" viewBox="0 0 60 60"><circle cx="24" cy="34" r="14" fill="none" stroke="#fff" stroke-width="8" stroke-dasharray="6 4"/><circle cx="24" cy="34" r="6" fill="#fff"/><circle cx="44" cy="16" r="9" fill="none" stroke="#fff" stroke-width="6" stroke-dasharray="5 3"/><circle cx="44" cy="16" r="3" fill="#fff"/></svg></div>
      <h3>Online Automation</h3><p>Add our web banners on your website. Your customers click on the banner to...</p>
    </div>
    <div class="way">
      <div class="way-icon"><svg width="60" height="56" viewBox="0 0 60 56"><path d="M4 4h52v36H24L12 52V40H4z" fill="none" stroke="#fff" stroke-width="4" stroke-linejoin="round"/><line x1="14" y1="16" x2="46" y2="16" stroke="#fff" stroke-width="3"/><line x1="14" y1="26" x2="40" y2="26" stroke="#fff" stroke-width="3"/></svg></div>
      <h3>Sms</h3><p>Send sms-certificates through text messaging with just one click! {{COMING SOON}}</p>
    </div>
  </div>
</section>

<section class="boost">
  <div class="boost-copy">
    <h2>Boost Response Rates To Your Existing Ads:</h2>
    <p>By adding one extra tagline: "Call for a Free Quote and receive a Three Day Two Night Hotel Stay Certificate to Las Vegas or 50 + other popular destinations, No Purchase Necessary." Imagine how many more leads you could generate.</p>
  </div>
  <div class="boost-photo-a" role="img" aria-label="Traveller in a sun hat sitting on a wooden dock before a lakeside temple"></div>
  <div class="boost-photo-b" role="img" aria-label="Hands typing on a silver laptop beside a bright window"></div>
</section>

<section class="plug" role="img" aria-label="Team of smiling professionals behind a blue overlay">
  <h2 class="section-title">We Plug Right Into Your Existing Business Model<br>In 4 Ways:</h2>
  <div class="plug-grid">
    <div class="plug-item"><div class="plug-icon"><svg width="50" height="44" viewBox="0 0 50 44"><path d="M6 14h10L38 2v40L16 30H6z" fill="#fff"/><rect x="12" y="30" width="8" height="12" fill="#fff"/><path d="M42 14q6 8 0 16" fill="none" stroke="#fff" stroke-width="3"/></svg></div><h3>Advertising</h3></div>
    <div class="plug-item"><div class="plug-icon"><svg width="48" height="48" viewBox="0 0 48 48"><circle cx="14" cy="9" r="6" fill="#fff"/><circle cx="34" cy="9" r="6" fill="#fff"/><rect x="7" y="17" width="14" height="29" rx="3" fill="#fff"/><rect x="27" y="17" width="14" height="29" rx="3" fill="#fff"/><path d="M20 26h8" stroke="#3b3d40" stroke-width="3"/></svg></div><h3>Residual Business</h3></div>
    <div class="plug-item"><div class="plug-icon"><svg width="48" height="44" viewBox="0 0 48 44"><rect x="4" y="30" width="7" height="12" fill="#fff"/><rect x="15" y="22" width="7" height="20" fill="#fff"/><rect x="26" y="16" width="7" height="26" fill="#fff"/><rect x="37" y="8" width="7" height="34" fill="#fff"/><path d="M4 22 18 10l8 6L42 2" fill="none" stroke="#fff" stroke-width="3"/></svg></div><h3>Sales</h3></div>
    <div class="plug-item"><div class="plug-icon"><svg width="54" height="40" viewBox="0 0 54 40"><path d="M2 10l12-6 10 6 8-4 20 8-8 14-12 8-14-10-12-2z" fill="#fff"/><path d="M24 10l-6 8 6 2 8-6" fill="none" stroke="#3b3d40" stroke-width="2.5"/></svg></div><h3>Referrals</h3></div>
  </div>
  <div class="plug-tip">Remind past clients about your products &amp; services with a 2 Night Mini of your previous business clients using a personal touch and an incentive to boot.</div>
</section>

<section class="clients">
  <h2 class="section-title">Our <em>Clients</em></h2>
  <div class="clients-grid">
    <div class="client"><i></i>Harborline Realty</div>
    <div class="client">ValueNest</div>
    <div class="client"><i></i>Corvane Motors</div>
    <div class="client">Skyreach TV</div>
  </div>
</section>

<section class="cta">
  <h2>Give Away An Unlimited Amount Of<br>Certificates To Your Customers<br><span>For Just $99 Bucks A Month.</span></h2>
  <a class="btn-dark" href="#">LEARN MORE</a>
</section>

<footer class="site-footer">
  <div class="to-top"><svg width="44" height="44" viewBox="0 0 44 44"><path d="M15 22l7-7 7 7M15 29l7-7 7 7" fill="none" stroke="#111" stroke-width="2.5"/></svg></div>
  <div class="footer-brand"><span class="brand-square"></span><span class="brand-name">Brightlane Promoworks</span></div>
  <p class="copyright">© <b>Brightlane Promoworks</b> - 2017. All Rights Reserved.</p>
</footer>

</body>
</html>
```